Serena Alba Candle Box Package Design

Two box sizes:
14oz Candle in a box Gift Boxes - 4 x 4 x 6
4oz Candle in a box Gift Boxes - 3 x 3 x 3
Website: www.serenaalba-example.com
IG: @serena.alba
My brand is a sophisticated brand with luxury candles made of coconut wax.  Serena Alba means bright life. Our candles represent hope and light.
You matter, you are worthy, powerful and beautiful!
Each candle is hand poured, vegan, environmentally conscious, uniquely scented and rooted in the importance of self care and community. We donate a percentage of our proceeds to organizations that seek to empower and enrich women.
At Serena Alba, we believe that positive energy can move mountains.
We strive to elevate that energy in every way possible. Our candles are handmade with confident positivity in mind - 100% vegan friendly, non-toxic and carefully crafted for optimal performance yet minimal impact on the environment.

```html
<!DOCTYPE html>
<html lang="en">
<head>
<meta charset="utf-8">
<title>Serena Alba – Simple Fold Box Dieline</title>
<link rel="stylesheet" href="https://fonts.googleapis.com/css2?family=Allison&family=Cormorant+Garamond:wght@300&family=Montserrat:wght@300;400&display=swap">
<style>
  :root {
    --page: #ffffff;
    --ink: #1d1d1f;
    --title-ink: #2f3142;
    --cut-line: #4a4a4a;
    --panel-light: #ffffff;
    --panel-mid: #f1f0f1;
    --panel-shade: #e4e3e5;
    --badge: #cfcfd2;
  }
  html, body {
    margin: 0;
    padding: 0;
    width: 809px;
    height: 1200px;
    overflow: hidden;
    background: var(--page);
  }
  .dieline { display: block; width: 809px; height: 1200px; }
  .panel { stroke: var(--cut-line); stroke-width: 1; }
  .sheet-title {
    font-family: "Cormorant Garamond", serif;
    font-weight: 300;
    font-size: 64px;
    letter-spacing: 7px;
    fill: var(--title-ink);
  }
  .body-copy {
    font-family: "Montserrat", sans-serif;
    font-weight: 300;
    font-size: 10.5px;
    letter-spacing: 0.6px;
    fill: var(--ink);
    text-anchor: middle;
  }
  .script {
    font-family: "Allison", cursive;
    fill: var(--ink);
    text-anchor: middle;
  }
  .quote { font-size: 34px; }
  .tagline-script { font-size: 30px; }
  .product-name { font-size: 84px; }
  .brand-name {
    font-family: "Montserrat", sans-serif;
    font-weight: 300;
    fill: var(--ink);
    text-anchor: middle;
    letter-spacing: 1px;
  }
  .brand-small { font-size: 17px; }
  .brand-large { font-size: 25px; letter-spacing: 2px; }
  .brand-sub {
    font-family: "Montserrat", sans-serif;
    font-weight: 400;
    font-size: 6.5px;
    letter-spacing: 1.6px;
    fill: var(--ink);
    text-anchor: middle;
  }
  .brand-love { font-size: 13px; }
  .net-weight {
    font-family: "Montserrat", sans-serif;
    font-weight: 400;
    font-size: 12.5px;
    letter-spacing: 1px;
    fill: var(--ink);
    text-anchor: middle;
  }
  .contact {
    font-family: "Montserrat", sans-serif;
    font-weight: 400;
    font-size: 16px;
    letter-spacing: 1.4px;
    fill: var(--ink);
  }
  .contact-dot { fill: none; stroke: var(--ink); stroke-width: 1.4; }
  .rule { stroke: var(--ink); stroke-width: 0.8; }
  .badge { fill: none; stroke: var(--badge); stroke-width: 1; }
</style>
</head>
<body>
<svg class="dieline" viewBox="40 505 1490 2210" xmlns="http://www.w3.org/2000/svg">
  <defs>
    <linearGradient id="panel-wash" x1="0" y1="0" x2="1" y2="1">
      <stop offset="0" stop-color="var(--panel-mid)"/>
      <stop offset="0.45" stop-color="var(--panel-light)"/>
      <stop offset="0.8" stop-color="var(--panel-mid)"/>
      <stop offset="1" stop-color="var(--panel-shade)"/>
    </linearGradient>
  </defs>

  <text class="sheet-title" x="180" y="1026">SIMPLE FOLD BOX</text>

  <g class="panels" fill="url(#panel-wash)" role="img" aria-label="Soft white and pale grey flowing silk wave pattern across all box panels">
    <!-- top flaps -->
    <rect class="panel" x="70" y="1188" width="335" height="300"/>
    <path class="panel" d="M408 1488 L415 1392 Q417 1362 447 1362 L700 1362 Q730 1362 732 1392 L738 1488 Z"/>
    <rect class="panel" x="740" y="1153" width="335" height="335"/>
    <path class="panel" d="M740 1153 L740 1100 Q740 1058 782 1058 L1033 1058 Q1075 1058 1075 1100 L1075 1153 Z"/>
    <path class="panel" d="M1078 1488 L1085 1392 Q1087 1362 1117 1362 L1370 1362 Q1400 1362 1402 1392 L1408 1488 Z"/>
    <!-- main row -->
    <rect class="panel" x="70" y="1488" width="335" height="335"/>
    <rect class="panel" x="405" y="1488" width="335" height="335"/>
    <rect class="panel" x="740" y="1488" width="335" height="335"/>
    <rect class="panel" x="1075" y="1488" width="335" height="335"/>
    <path class="panel" d="M1410 1488 L1488 1500 Q1495 1501 1495 1510 L1495 1800 Q1495 1809 1488 1810 L1410 1823 Z"/>
    <!-- bottom flaps -->
    <path class="panel" d="M75 1823 L400 1823 L400 2078 Q400 2118 360 2118 L115 2118 Q75 2118 75 2078 Z"/>
    <rect class="panel" x="405" y="1823" width="335" height="335"/>
    <path class="panel" d="M405 2158 L740 2158 L740 2212 Q740 2252 700 2252 L445 2252 Q405 2252 405 2212 Z"/>
    <path class="panel" d="M745 1823 L1070 1823 L1070 2078 Q1070 2118 1030 2118 L785 2118 Q745 2118 745 2078 Z"/>
  </g>

  <!-- message flap -->
  <g class="message-flap">
    <text class="script quote" x="237" y="1262">Our candles</text>
    <text class="script quote" x="237" y="1303">represent hope and light</text>
    <text class="script quote" x="237" y="1388">You matter, you are worthy,</text>
    <text class="script quote" x="237" y="1428">powerful and beautiful!</text>
  </g>

  <!-- top lid -->
  <text class="brand-name brand-large" x="907" y="1332">SERENA ALBA</text>

  <!-- story side -->
  <g class="story-side">
    <text class="body-copy" x="572" y="1532">EACH CANDLE IS HAND POURED, VEGAN,</text>
    <text class="body-copy" x="572" y="1545">ENVIRONMENTALLY CONSCIOUS, UNIQUELY SCENTED</text>
    <text class="body-copy" x="572" y="1558">AND ROOTED IN THE IMPORTANCE OF SELF CARE</text>
    <text class="body-copy" x="572" y="1571">AND COMMUNITY.</text>
    <text class="body-copy" x="572" y="1584">WE DONATE A PERCENTAGE OF OUR PROCEEDS TO</text>
    <text class="body-copy" x="572" y="1597">ORGANIZATIONS THAT SEEK TO EMPOWER AND</text>
    <text class="body-copy" x="572" y="1610">ENRICH WOMEN.</text>
    <text class="body-copy" x="572" y="1635">AT SERENA ALBA, WE BELIEVE THAT POSITIVE</text>
    <text class="body-copy" x="572" y="1648">ENERGY CAN MOVE MOUNTAINS.</text>
    <line class="rule" x1="522" y1="1664" x2="622" y2="1664"/>
    <text class="script tagline-script" x="572" y="1694">We strive to elevate that energy in every way possible</text>
    <line class="rule" x1="522" y1="1716" x2="622" y2="1716"/>
    <text class="body-copy" x="572" y="1735">OUR CANDLES ARE HANDMADE WITH CONFIDENT</text>
    <text class="body-copy" x="572" y="1748">POSITIVITY IN MIND - 100% VEGAN FRIENDLY,</text>
    <text class="body-copy" x="572" y="1761">NON-TOXIC &amp; CAREFULLY CRAFTED</text>
    <text class="body-copy" x="572" y="1774">FOR OPTIMAL PERFORMANCE</text>
    <text class="body-copy" x="572" y="1787">YET MINIMAL IMPACT ON THE ENVIRONMENT.</text>
  </g>

  <!-- front -->
  <g class="front-face">
    <text class="brand-name brand-small" x="907" y="1535">SERENA ALBA</text>
    <text class="brand-sub" x="907" y="1549">— HANDMADE CANDLES —</text>
    <text class="script brand-love" x="907" y="1560">with purpose and love</text>
    <circle class="badge" cx="1040" cy="1529" r="24"/>
    <text class="script product-name" x="907" y="1688">Quiet Grove</text>
    <text class="net-weight" x="907" y="1808">14oz. (396g)</text>
  </g>

  <!-- notes side -->
  <g class="notes-side">
    <text class="body-copy" x="1243" y="1566">NOBLE FIR</text>
    <text class="body-copy" x="1243" y="1582">RED PINE</text>
    <text class="body-copy" x="1243" y="1598">PALO SANTO</text>
    <text class="body-copy" x="1243" y="1614">OAKMOSS</text>
    <text class="body-copy" x="1243" y="1630">JUNIPER</text>
    <line class="rule" x1="1178" y1="1647" x2="1308" y2="1647"/>
    <text class="body-copy" x="1243" y="1670">BURN TIME UP TO 70HRS</text>
    <text class="body-copy" x="1243" y="1686">NATURAL COCONUT WAX</text>
    <text class="body-copy" x="1243" y="1702">SKIN SAFE</text>
    <text class="body-copy" x="1243" y="1718">SLOW CLEAN-BURNING</text>
    <text class="body-copy" x="1243" y="1734">PET FRIENDLY</text>
    <text class="body-copy" x="1243" y="1750">NON-TOXIC | PHTHALATE-FREE | PARABEN-FREE</text>
  </g>

  <!-- contact flap -->
  <g class="contact-block">
    <circle class="contact-dot" cx="448" cy="1978" r="8.5"/>
    <text class="contact" x="464" y="1984">www.serenaalba-example.com</text>
    <circle class="contact-dot" cx="448" cy="2004" r="8.5"/>
    <text class="contact" x="464" y="2010">@serena.alba</text>
  </g>
</svg>
</body>
</html>
```